Business Card Design with new logo

Dorian Pelleway 4172
E 118th St Brackton, IL 62488
Cell: 217-555-0193
pellewayrestoration@mailvane.test

Classic Car Restoration Services Buy Sell Trade Consign

Dorian Pelleway 9698
Cell: 217-555-0193

```html
<!DOCTYPE html>
<html lang="en">
<head>
<meta charset="utf-8">
<title>Pelleway Restoration LLC – Business Cards</title>
<link href="https://fonts.googleapis.com/css2?family=Roboto:wght@300;400;700;900&display=swap" rel="stylesheet">
<style>
  :root {
    --navy: #13222f;
    --red: #e3312f;
    --white: #ffffff;
    --ink: #1d2731;
    --grey: #4d5660;
    --backdrop: #4a433e;
  }
  * { box-sizing: border-box; margin: 0; padding: 0; }
  html, body { width: 1200px; height: 930px; overflow: hidden; }
  body {
    background: var(--backdrop);
    font-family: "Roboto", Arial, sans-serif;
    position: relative;
  }
  .card {
    position: absolute;
    width: 560px;
    height: 320px;
    border-radius: 14px;
    overflow: hidden;
    box-shadow: 0 10px 24px rgba(0,0,0,0.35);
  }
  /* Back of card */
  .card-back {
    left: 80px;
    top: 90px;
    background: var(--navy);
    display: flex;
    align-items: center;
    justify-content: center;
  }
  .wordmark {
    display: flex;
    align-items: center;
    gap: 14px;
  }
  .wordmark-dot {
    width: 26px;
    height: 26px;
    border-radius: 50%;
    background: var(--red);
    flex: none;
  }
  .wordmark-text {
    font-weight: 900;
    line-height: 1;
    text-transform: uppercase;
  }
  .wordmark-name { display: block; font-size: 44px; letter-spacing: 1px; }
  .wordmark-sub { display: block; font-size: 15px; letter-spacing: 9px; margin-top: 8px; }
  .card-back .wordmark-text { color: var(--white); }

  /* Front of card */
  .card-front {
    left: 560px;
    top: 500px;
    background: var(--white);
  }
  .card-front .wordmark {
    position: absolute;
    left: 36px;
    top: 58px;
  }
  .card-front .wordmark-text { color: var(--navy); }
  .card-front .wordmark-name { font-size: 34px; }
  .card-front .wordmark-sub { font-size: 12px; letter-spacing: 7px; }

  .holder {
    position: absolute;
    right: 36px;
    top: 42px;
    text-align: right;
  }
  .holder-name {
    color: var(--red);
    font-size: 30px;
    font-weight: 400;
    text-transform: uppercase;
    letter-spacing: -0.5px;
  }
  .holder-role {
    color: var(--grey);
    font-size: 14px;
    font-weight: 300;
    margin-top: 2px;
  }
  .rule {
    position: absolute;
    height: 2px;
    background: var(--red);
  }
  .rule-name { right: 30px; top: 118px; width: 300px; }
  .rule-contact { left: 30px; top: 198px; width: 270px; }

  .address {
    position: absolute;
    right: 36px;
    top: 150px;
    text-align: right;
    color: var(--ink);
    font-size: 15px;
    font-weight: 300;
    line-height: 1.35;
  }
  .contacts {
    position: absolute;
    left: 34px;
    top: 210px;
    list-style: none;
    color: var(--ink);
    font-size: 15px;
    font-weight: 300;
    line-height: 1.45;
  }
  .contacts li { display: flex; align-items: center; gap: 8px; }
  .contacts svg { width: 11px; height: 11px; flex: none; }
  .contacts .accent { color: var(--red); }
  .footer-band {
    position: absolute;
    left: 0;
    bottom: 0;
    width: 560px;
    height: 70px;
  }
</style>
</head>
<body>

  <section class="card card-back" aria-label="Card back">
    <div class="wordmark">
      <span class="wordmark-dot"></span>
      <span class="wordmark-text">
        <span class="wordmark-name">Pelleway</span>
        <span class="wordmark-sub">Restoration LLC</span>
      </span>
    </div>
  </section>

  <section class="card card-front" aria-label="Card front">
    <div class="wordmark">
      <span class="wordmark-dot"></span>
      <span class="wordmark-text">
        <span class="wordmark-name">Pelleway</span>
        <span class="wordmark-sub">Restoration LLC</span>
      </span>
    </div>

    <div class="holder">
      <p class="holder-name">Rowan Ellery</p>
      <p class="holder-role">Director</p>
    </div>
    <div class="rule rule-name"></div>

    <p class="address">Dorian Pelleway 4172<br>E 118th St Brackton, IL 62488</p>

    <div class="rule rule-contact"></div>
    <ul class="contacts">
      <li>
        <svg viewBox="0 0 12 12" aria-hidden="true"><path d="M2.5 1 L4.5 1 L5.2 3.6 L4 4.6 Q5 7 7.4 8 L8.4 6.8 L11 7.5 L11 9.5 Q10.5 11 9 11 Q1 10 1 2.8 Q1 1 2.5 1Z" fill="#e3312f"/></svg>
        <span>217-555-0193</span>
      </li>
      <li>
        <svg viewBox="0 0 12 12" aria-hidden="true"><rect x="1" y="2.5" width="10" height="7" fill="none" stroke="#e3312f" stroke-width="1.3"/><path d="M1 2.5 L6 6.5 L11 2.5" fill="none" stroke="#e3312f" stroke-width="1.3"/></svg>
        <span>pellewayrestoration@mailvane.test</span>
      </li>
      <li>
        <svg viewBox="0 0 12 12" aria-hidden="true"><circle cx="6" cy="6" r="5" fill="none" stroke="#e3312f" stroke-width="1.2"/><ellipse cx="6" cy="6" rx="2.2" ry="5" fill="none" stroke="#e3312f" stroke-width="1"/><path d="M1 6 H11" stroke="#e3312f" stroke-width="1"/></svg>
        <span>www.<span class="accent">pellewayrestoration</span>.test</span>
      </li>
    </ul>

    <svg class="footer-band" viewBox="0 0 560 70" aria-hidden="true">
      <path d="M0 70 L0 62 L360 62 Q382 62 392 46 Q404 22 430 22 L560 22 L560 70 Z" fill="#13222f"/>
      <path d="M0 52 L356 52 Q374 52 382 40 L388 40 Q378 58 356 58 L0 58 Z" fill="#e3312f"/>
    </svg>
  </section>

</body>
</html>
```